Paleo Diet Book Cover Design

I need a cover designed for my book Stone Frame that will be sold on Rivora Pageleaf and other sites. So the front, side and back will need to be designed. I have attached part of the book here so feel free to skim through the content and give it a quick read to get a feel for what the book is about. Stone Frame is about eating the diet of the caveman (paleolithic era-paleo) and a 12 week workout plan with a grocery shopping list and meal plans. It is for men and women ages 18+ who are interested in health and fitness and becoming healthier overall.
The graphics should be secondary, and it should add to the text, not distract from it. This is even more important because the size of the cover displayed on Rivora/Pageleaf, when your book is first seen by a potential buyer, is so tiny. It's barely an inch high, and even smaller in width.
So the words have to be big, bold, benefit-rich and easy to read. That also means, don't mess with the fancy fonts. Clean, clear, crisp font is best. And, did I say BIG already?
Contrast the colors of the text and background, so its even easier to read. That means, dark text on light background or visa versa. Colors like darker reds, blues / teals and oranges.
Please read this: http://www.bookvantrel.com/8-cover-design-secrets-publishers-use-to-manipulate-readers-into-buying-books/
The cover has to be bold and easy to read, it has to stick out, it has to draw the attention of your readers so that they zero in on my book, out of all the other books on the page. (Much like they would when viewing a classified ads site/page.)
The Title of the Book is Stone Frame, and the subtitle is "Transform Your Body For Life in 12 Weeks With Proven Workouts and Paleo Diet Based Nutrition" Perhaps “Transform Your Body For Life in 12 Weeks” could also be in a large font similar to the title with the rest of the subtitle following afterwards. You can try having the title be the smaller font with the subtitle being the larger font as well.
Then the authors name "Colin Marsh” incorporated into the design.
I am not sure what to use as the background type of design for the front of the book so feel free to be creative with that.
The size needs to be 1563 pixels on the shortest side and 2500 pixels on the longest side just for the front of the cover.

```html
<!DOCTYPE html>
<html lang="en">
<head>
<meta charset="utf-8">
<title>Stone Frame – Book Cover</title>
<link href="https://fonts.googleapis.com/css2?family=Bebas+Neue&family=Open+Sans:wght@700&family=Patrick+Hand+SC&display=swap" rel="stylesheet">
<style>
  :root {
    --cover-red-light: #e61e27;
    --cover-red-mid: #cf1820;
    --cover-red-dark: #ab1016;
    --title-yellow: #fcd10b;
    --subtitle-peach: #f2a772;
    --figure-peach: #f6b892;
    --author-white: #ffffff;
  }
  html, body {
    margin: 0;
    padding: 0;
    width: 750px;
    height: 1200px;
    overflow: hidden;
    background: var(--cover-red-dark);
  }
  .cover {
    position: relative;
    width: 750px;
    height: 1200px;
    overflow: hidden;
    background: radial-gradient(ellipse 520px 640px at 300px 420px, var(--cover-red-light) 0%, var(--cover-red-mid) 55%, var(--cover-red-dark) 100%);
  }
  .book-title {
    position: absolute;
    width: 1px;
    height: 1px;
    overflow: hidden;
    clip: rect(0 0 0 0);
    margin: 0;
  }
  .cover-art {
    position: absolute;
    left: 0;
    top: 0;
    width: 750px;
    height: 1200px;
  }
  .title-line {
    font-family: "Bebas Neue", "Oswald", sans-serif;
    font-size: 400px;
    fill: var(--title-yellow);
  }
  .subtitle-line {
    font-family: "Patrick Hand SC", "Patrick Hand", cursive;
    font-size: 60px;
    fill: var(--subtitle-peach);
  }
  .author-name {
    position: absolute;
    left: 0;
    right: 0;
    top: 1062px;
    margin: 0;
    text-align: center;
    font-family: "Open Sans", Arial, sans-serif;
    font-weight: 700;
    font-size: 66px;
    line-height: 1;
    color: var(--author-white);
  }
</style>
</head>
<body>
  <main class="cover">
    <h1 class="book-title">Stone Frame</h1>
    <svg class="cover-art" viewBox="0 0 750 1200" xmlns="http://www.w3.org/2000/svg" aria-hidden="false">
      <rect class="leaping-figure" role="img" aria-label="Peach silhouette of a leaping athlete woven into the title" x="246" y="346" width="110" height="416" rx="46" fill="#f6b892"/>
      <text class="title-line" x="59" y="352" textLength="632" lengthAdjust="spacingAndGlyphs">STONE</text>
      <text class="title-line" x="59" y="720" textLength="632" lengthAdjust="spacingAndGlyphs">FRAME</text>
      <text class="subtitle-line" x="64" y="826" textLength="616" lengthAdjust="spacingAndGlyphs">TRANSFORM YOUR BODY</text>
      <text class="subtitle-line" x="70" y="920" textLength="600" lengthAdjust="spacingAndGlyphs">FOR LIFE IN 12 WEEKS</text>
    </svg>
    <p class="author-name">Colin Marsh</p>
  </main>
</body>
</html>
```